VarnLink Signal Systems Website Design

We are an Australian based telecommunications company who specialise in the design, build and implementation of mission critical communications infrastructure. We have offices throughout Australia, New Zealand and Europe. Our Customers are operators in multiple markets from Oil & Gas, Mining, Government, Utilities, Carrier & Transportation.

We also work with large multi-national companies, that provide telecommunication and services such as; Pelvaro, Dransvik, Quorba, Talmoss and many more. We want to be able to achieve the same level of impressions and professionalism as what these companies present on their websites.

To reflect our recent move into the European market, we need our new site to reflect who we are as a company, and exhibit the fact we are not just based in Australia, but we are a global organisation. We want to have a fresh clean look, thats modern, dynamic and simple. Flat textures and colours are perfect for us to adapt to. A site that is based around content management, with a responsive design that can be used on all devices.

We have started to develop a basic design language that we would like to incorporate in our overall website design. We have attached some documents that highlight our design language and we can provide colour codes and fonts to ensure consistency.

Our existing site is: www.varnlinkss.example. Please feel free to view and pick apart items. From this example, we would massive improvement in how the site looks, feels and functions. We also want social media to form a big part of our site, with the likes of posts from chirpnet and blogs posting capabilities.

If you require anymore information about VarnLink or our requirements, please do not hesitate to contact.

Thanks and good luck!

Target Market(s)

Potential & Existing Customers, New international customers & markets, New Market Sectors, Partners, Service Providers

Industry/Entity Type

Telecommunications

Coding

Coded - Design and coding required

Number of Pages Required

5+ page

Font styles to use
Sans Serif

Requirements
Must have
• Content Management, Responsive Design for multiple device compatibility, Social media integration, use of lots of imagery, drop down menus, search capabilities
Should not have
• No flash.

```html
<!DOCTYPE html>
<html lang="en">
<head>
<meta charset="utf-8">
<title>VarnLink Signal Systems</title>
<link href="https://fonts.googleapis.com/css2?family=Raleway:wght@400;500;600;700;800&family=Open+Sans:wght@400;600;700&display=swap" rel="stylesheet">
<style>
:root{
  --navy:#24305e;
  --navy-dark:#1c2650;
  --purple:#6f73b8;
  --blue-link:#4a63b0;
  --orange:#f7941d;
  --teal:#4fbfae;
  --grey:#6d6e71;
  --light:#f0f1f4;
  --text:#6a6e78;
  --white:#ffffff;
}
*{box-sizing:border-box;margin:0;padding:0}
html,body{width:1200px;height:3080px;overflow:hidden;background:var(--white)}
body{font-family:"Open Sans",Arial,sans-serif;color:var(--text);font-size:13px;position:relative}
h1,h2,h3,h4,.nav,.btn,.label{font-family:"Raleway",Arial,sans-serif}

/* header */
.site-header{height:68px;display:flex;align-items:center;padding:0 60px 0 80px;position:relative}
.brand{font-family:"Raleway",sans-serif;font-weight:800;font-size:30px;color:var(--navy);display:flex;align-items:center;gap:8px}
.brand-dot{width:12px;height:12px;border-radius:50%;background:var(--purple)}
.header-right{margin-left:auto;display:flex;flex-direction:column;align-items:flex-end;gap:8px}
.quick-buttons{display:flex;gap:10px}
.quick-buttons span{border:1px solid #c8cbe0;color:var(--navy);font-size:9px;font-weight:700;padding:4px 14px;letter-spacing:.5px;font-family:"Raleway",sans-serif}
.nav{display:flex;gap:26px;font-size:11px;font-weight:700;color:var(--navy);letter-spacing:.4px}
.nav .active{color:#9aa0bf;border-bottom:2px solid var(--purple);padding-bottom:3px}

/* hero */
.hero{position:relative;height:572px;background:linear-gradient(100deg,#8b98a8 0%,#c9cfd6 45%,#e7e3d9 70%,#b7b3a6 100%);overflow:hidden}
.hero-copy{position:absolute;left:60px;top:40px;width:600px;color:var(--white)}
.hero-copy h1{font-size:42px;font-weight:800;line-height:1.05;letter-spacing:1px;text-shadow:0 1px 3px rgba(0,0,0,.25)}
.hero-copy p{margin-top:14px;font-size:16px;line-height:1.45;font-weight:600;text-shadow:0 1px 2px rgba(0,0,0,.3)}
.btn{display:inline-block;background:var(--purple);color:var(--white);font-size:12px;font-weight:600;padding:9px 20px;margin-top:22px}
.hero-dots{position:absolute;left:560px;top:565px;display:flex;gap:8px}
.hero-dots i{width:8px;height:8px;border-radius:50%;background:#cfd3e2}
.hero-dots i:first-child{background:var(--purple)}
.cert-badges{position:absolute;right:30px;top:470px;display:flex;gap:10px}
.cert-badges i{width:52px;height:40px;background:#efc94c}
.hero-ribbon{position:absolute;left:0;right:0;bottom:0;height:60px;background:var(--light);clip-path:polygon(0 70%,100% 0,100% 100%,0 100%)}

/* service boxes */
.services{background:var(--light);height:520px;position:relative}
.service-row{position:absolute;left:60px;top:40px;display:flex;gap:40px}
.service{width:240px;height:440px;color:var(--white);text-align:center;padding:120px 24px 0;clip-path:polygon(0 0,100% 0,100% 94%,0 100%)}
.service.orange{background:var(--orange)}
.service.teal{background:var(--teal);clip-path:polygon(0 6%,100% 0,100% 100%,0 94%)}
.service.grey{background:var(--grey);clip-path:polygon(0 0,100% 6%,100% 100%,0 100%)}
.service svg{display:block;margin:0 auto 26px}
.service h3{font-size:17px;font-weight:700;letter-spacing:.5px}
.service p{font-size:12px;line-height:1.5;margin-top:10px;opacity:.9}
.service-wrap{position:relative}
.service-wrap .hang{position:absolute;left:0;right:0;top:440px;height:48px}

/* about */
.about{height:300px;position:relative;background:var(--white)}
.about-copy{position:absolute;left:60px;top:20px;width:600px}
.about-copy h4{font-size:15px;font-weight:700;color:#8a8ea0;letter-spacing:.5px}
.about-copy h2{font-size:22px;font-weight:800;color:var(--navy);letter-spacing:.5px}
.about-copy p{margin-top:16px;font-size:12px;line-height:1.65}
.about-photo{position:absolute;right:60px;top:-20px;width:400px;height:320px;background:linear-gradient(160deg,#3c5575 0%,#7a95b6 40%,#c6d4e2 70%,#5f6b7a 100%)}

/* vision */
.vision{height:320px;background:linear-gradient(180deg,#30374a,#1d2233);position:relative;color:#c5c9d6;text-align:center;padding:92px 100px 0;clip-path:polygon(0 12%,100% 0,100% 100%,0 100%)}
.vision .map{position:absolute;inset:0;background:radial-gradient(ellipse at 50% 55%,rgba(120,130,160,.25),transparent 65%)}
.vision h2{position:relative;font-size:24px;color:var(--purple);font-weight:700}
.vision p{position:relative;margin-top:14px;font-size:12px;line-height:1.7}

/* markets */
.markets{height:400px;text-align:center;padding-top:36px;position:relative}
.section-title{font-size:20px;font-weight:800;color:var(--navy);letter-spacing:.5px}
.section-intro{font-size:12px;line-height:1.7;margin:10px auto 0;width:760px}
.market-row{display:flex;justify-content:center;gap:28px;margin-top:30px;align-items:center}
.arrow{width:30px;height:30px;display:flex;align-items:center;justify-content:center}
.market{width:220px}
.market .photo{height:140px}
.market .label{margin-top:14px;font-size:14px;font-weight:700;color:var(--orange);letter-spacing:.5px}

/* clients */
.clients{height:240px;background:var(--light);text-align:center;padding-top:36px}
.client-row{display:flex;justify-content:space-around;align-items:center;margin:48px 60px 0}
.client{display:flex;align-items:center;gap:10px;font-family:"Raleway",sans-serif;font-weight:800;font-size:30px;color:var(--navy)}
.client i{width:14px;height:14px;background:var(--purple)}

/* blog & feed */
.news{height:320px;display:flex;padding:32px 60px 0;gap:60px}
.news h3{font-size:19px;font-weight:800;color:var(--navy);letter-spacing:.5px;margin-bottom:20px}
.blog{width:620px}
.post{display:flex;gap:20px;margin-bottom:22px}
.post .thumb{width:180px;height:100px;flex:none}
.post h4{font-size:13px;color:var(--blue-link);font-weight:700}
.post p{font-size:11px;line-height:1.55;margin-top:6px}
.post .more{font-size:10px;color:#a3a7b8;margin-top:6px}
.feed{flex:1}
.tweet{display:flex;gap:16px;margin-bottom:30px;border-bottom:1px solid #e3e5ec;padding-bottom:20px}
.tweet .avatar{width:80px;height:48px;flex:none;border:1px solid #dde0ea;display:flex;align-items:center;justify-content:center;font-family:"Raleway",sans-serif;font-weight:800;font-size:12px;color:var(--navy)}
.tweet h4{font-size:12px;color:var(--blue-link);font-weight:700}
.tweet p{font-size:11px;line-height:1.5;margin-top:4px}

/* footer */
.site-footer{position:absolute;left:0;right:0;bottom:0;height:360px;background:var(--navy);color:#b5bbd4;clip-path:polygon(0 8%,100% 0,100% 100%,0 100%);padding:70px 60px 0;display:flex;gap:40px}
.footer-brand{width:260px}
.footer-brand .brand{color:var(--white)}
.footer-brand p{font-size:11px;line-height:1.6;margin-top:30px}
.footer-col h4{font-size:12px;font-weight:700;color:var(--white);letter-spacing:.5px;margin-bottom:12px}
.footer-col ul{list-style:none;font-size:11px;line-height:2}
.link-cols{display:flex;gap:40px}
.social{display:flex;gap:8px}
.social i{width:26px;height:26px;border-radius:50%;border:1px solid #8e96bb}
</style>
</head>
<body>

<header class="site-header">
  <div class="brand"><span class="brand-dot"></span>VarnLink</div>
  <div class="header-right">
    <div class="quick-buttons"><span>SERVICE DESK ›</span><span>RMA REPAIR STATUS ›</span></div>
    <nav class="nav">
      <span class="active">HOME</span><span>PRODUCTS &amp; SERVICES</span><span>SECTORS</span><span>SUPPORT</span><span>CORPORATE</span><span>CONTACT</span>
    </nav>
  </div>
</header>

<section class="hero" role="img" aria-label="Engineers in hard hats and high-visibility vests reviewing plans on site">
  <div class="hero-copy">
    <h1>CERTIFIED TO THE HIGHEST<br>STANDARDS</h1>
    <p>We strive to achieve and meet the relevant standards to exceed our own and customer expectations. That's why we have recently been accredited for Health and Safety Certification AS4801/OHSAS18001 by Certra Assurance.</p>
    <span class="btn">Find Out More</span>
  </div>
  <div class="cert-badges"><i></i><i></i><i></i></div>
  <div class="hero-dots"><i></i><i></i><i></i><i></i></div>
  <div class="hero-ribbon"></div>
</section>

<section class="services">
  <div class="service-row">
    <div class="service orange">
      <svg width="90" height="70" viewBox="0 0 90 70" fill="#fff"><rect x="28" y="2" width="32" height="28"/><rect x="8" y="36" width="32" height="28"/><rect x="48" y="36" width="32" height="28"/></svg>
      <h3>PRODUCT &amp; SERVICES</h3>
      <p>Aliquam molestie, mi sit imperdiet euismod, dui purus auctor tellus, et interdum lacus lectus at elite.</p>
    </div>
    <div class="service teal">
      <svg width="90" height="70" viewBox="0 0 90 70" fill="none" stroke="#fff" stroke-width="4"><rect x="8" y="6" width="74" height="46"/><line x1="45" y1="52" x2="45" y2="64"/><line x1="28" y1="64" x2="62" y2="64"/><line x1="34" y1="38" x2="54" y2="20"/></svg>
      <h3>TECHNICAL SUPPORT</h3>
      <p>Aliquam molestie, mi sit imperdiet euismod, dui purus auctor tellus, et interdum lacus lectus at elite.</p>
    </div>
    <div class="service grey">
      <svg width="90" height="70" viewBox="0 0 90 70" fill="#fff"><rect x="10" y="40" width="12" height="26"/><rect x="28" y="26" width="12" height="40"/><rect x="46" y="34" width="12" height="32"/><rect x="64" y="10" width="12" height="56"/></svg>
      <h3>MARKET SECTORES</h3>
      <p>Aliquam molestie, mi sit imperdiet euismod, dui purus auctor tellus, et interdum lacus lectus at elite.</p>
    </div>
  </div>
</section>

<section class="about">
  <div class="about-copy">
    <h4>ABOUT</h4>
    <h2>VARNLINK SIGNAL SYSTEMS</h2>
    <p>VarnLink Signal Systems is an Australian owned company that provides turnkey communications solutions to customers around the world. Founded in 1998, the company has grown to be the leading supplier of communications systems and equipment in its field. Our core business covers the utilities and carrier markets, and we have succeeded in expanding our profile into the emergency services sector.</p>
    <span class="btn">Find Out More</span>
  </div>
  <div class="about-photo" role="img" aria-label="Modern glass office building against a blue sky"></div>
</section>

<section class="vision">
  <div class="map" role="img" aria-label="Faint world map"></div>
  <h2>Our Vision</h2>
  <p>Aliquam molestie, mi sit imperdiet euismod, dui purus auctor tellus, et interdum lacus lectus at ante. Sed accumsan sollicitudin sapien, sit amet adipiscing turpis gravida ac. Ut congue, neque ac lobortis volutpat, libero mauris viverra nisl, vel suscipit ipsum ligula vitae risus. Duis aliquam nibh a dui iaculis viverra et a nisl. Vivamus congue risus at magna varius commodo. Sed semper viverra egestas. Etiam pretium porttitor lectus, vel ornare neque pulvinar tempus.</p>
</section>

<section class="markets">
  <h2 class="section-title">OUR MARKETS</h2>
  <p class="section-intro">Aliquam molestie, mi sit imperdiet euismod, dui purus auctor tellus, et interdum lacus lectus at elite. Sed accumsan sollicitudin sapien, sit amet adipiscing turpis gravida ac.</p>
  <div class="market-row">
    <div class="arrow"><svg width="16" height="24" viewBox="0 0 16 24"><path d="M13 2 3 12l10 10" fill="none" stroke="#24305e" stroke-width="3"/></svg></div>
    <div class="market"><div class="photo" role="img" aria-label="Oil refinery at dusk" style="background:linear-gradient(160deg,#2e4a7a,#6a8cc0 60%,#e3a24a)"></div><div class="label">OIL &amp; GAS</div></div>
    <div class="market"><div class="photo" role="img" aria-label="Electricity pylons under a blue sky" style="background:linear-gradient(170deg,#4f86c6,#a9c8e6)"></div><div class="label">ELECTRICITY UTILITIES</div></div>
    <div class="market"><div class="photo" role="img" aria-label="Trucks on a highway" style="background:linear-gradient(160deg,#8d2c2c,#c45151 50%,#4f5d77)"></div><div class="label">TRANSPORT</div></div>
    <div class="market"><div class="photo" role="img" aria-label="Network cabling in a data rack" style="background:linear-gradient(160deg,#1f4f83,#4f9fd6 55%,#cfe4f2)"></div><div class="label">CARRIER</div></div>
    <div class="arrow"><svg width="16" height="24" viewBox="0 0 16 24"><path d="M3 2l10 10L3 22" fill="none" stroke="#24305e" stroke-width="3"/></svg></div>
  </div>
</section>

<section class="clients">
  <h2 class="section-title">OUR CLIENTS</h2>
  <div class="client-row">
    <span class="client">Dransvik</span>
    <span class="client">Quorba</span>
    <span class="client">Talmoss</span>
    <span class="client">Pelvaro</span>
    <span class="client">Veltrane</span>
  </div>
</section>

<section class="news">
  <div class="blog">
    <h3>BLOG POSTS</h3>
    <article class="post">
      <div class="thumb" role="img" aria-label="Solar panel array" style="background:linear-gradient(160deg,#2c4f86,#7fa4d0)"></div>
      <div><h4>Aliquam molestie, mi sit imperdiet euismod</h4><p>Dui purus auctor tellus, et interdum lacus lectus at ante. Sed accumsan sollicitudin sapien, sit amet adipiscing turpis gravida ac.</p><div class="more">Continue Reading</div></div>
    </article>
    <article class="post">
      <div class="thumb" role="img" aria-label="Technician working on equipment" style="background:linear-gradient(160deg,#3b4a3a,#8a9a6e)"></div>
      <div><h4>Aliquam molestie, mi sit imperdiet euismod</h4><p>Dui purus auctor tellus, et interdum lacus lectus at ante. Sed accumsan sollicitudin sapien, sit amet adipiscing turpis gravida ac.</p><div class="more">Continue Reading</div></div>
    </article>
  </div>
  <div class="feed">
    <h3>CHIRPNET FEEDS</h3>
    <div class="tweet"><div class="avatar">VarnLink</div><div><h4>VarnLink SS @varnlinkss · 2h</h4><p>Follow us on chirpnet for all the latest news and updates from VarnLink. #communications #networks</p></div></div>
    <div class="tweet"><div class="avatar">VarnLink</div><div><h4>VarnLink SS @varnlinkss · 1d</h4><p>Follow us on chirpnet for all the latest news and updates from VarnLink. #communications #networks</p></div></div>
  </div>
</section>

<footer class="site-footer">
  <div class="footer-brand">
    <div class="brand"><span class="brand-dot"></span>VarnLink</div>
    <p>Copyright © 2015<br>VarnLink Signal Systems<br>www.varnlinkss.example</p>
  </div>
  <div class="footer-col">
    <h4>QUICK LINKS</h4>
    <div class="link-cols">
      <ul><li>Partners &amp; Technology</li><li>Project Site Solutions</li><li>Innovation</li><li>R&amp;D</li><li>Case Studies</li><li>Careers</li></ul>
      <ul><li>Professional Services</li><li>Responsibilities</li><li>Support</li><li>Contact</li></ul>
    </div>
  </div>
  <div class="footer-col">
    <h4>OTHER LINKS</h4>
    <ul><li>Legal Information</li><li>Privacy Policy</li><li>Terms of Use</li><li>Cookies</li><li>Site Map</li></ul>
  </div>
  <div class="footer-col">
    <h4>CONNECT US</h4>
    <div class="social"><i></i><i></i><i></i><i></i><i></i></div>
  </div>
</footer>

</body>
</html>
```